#28 - On the Letterheadpaper, can you please make the footercolorfields littlebit darker? I mean the Colors are too bright compared to the Logocolors, or?!
@Torven #22 - Can you please add on the backside the url's like on #7 ?
@quembrastudio #18 - Businesscard: The footer (colored fields) maybe a little bit to strong/high, can you test it with 2-3px less? #18 - Letterheadpaper: Need the footer (colored fields) here! Looks without ... nacked. ;) #18 - Please add the "Back of the business card"-things what you can read in the briefing.
@quembrastudio #1#2 - Eliminated; Better draft available with #4 #11 - Eliminated; I think the logo is better on a "normal" business card style, and maybe thats are other card Dimensions. #10 #9 - The Black Symbols on the Businesscard is maybe to strong. Can you test it with blue or grey symbols? #4 - At the moment my favorite, but please the "84116 Grunwiesel" in a new line under the Street (businesscard), thats the correct format in Germany. I'm not so happy with the URL in the blue footerfield, maybe smaller or in a other location, I don't know?! Please put on the letterhead the Facts from the footer into the header (right under the Logo), maybe in a small/tiny clear Fonttype. The Flyerbusinesscard don't have the color fields on the bottom?
@torven #8 - Front looks nice, but the Logo on the backside is not strong/"clear" enough I think. #7#5 - Eliminated; Not my Style, Sorry. #6 - Eliminated; The footer (blue field) on the Front was to heavy
Can't vote for your drafts the Flyer and Letterhead are missing.
@vOlpt
Nice blue symbols on the Businesscard, but the color on the backside is purple, I think that kills the blue/grey Logo and Style on the Frontside. And the Logo with Name under it is one unit, either the Logo with the Name direct under the Logo, or the Logo standalone. :)
Cant't vote for your drafts, don't need Envelopes but the Flyer. ;)
@Marble314
Thanks for your Drafts, but it's not my Style and I think it's not the Style from the Logo, the heavy yellow Background "kills" the nice look of the Blue/Grey Logo, too.
#2 In Germany is it more standard that the Logo is on the right side.
Please make a new draft with the Logo on the right side and the personal data (Address) under the Logo. In the footer comes the web address and maybe later some bank account informations or a funny quote.
I miss in the Address the ID and the Name of the City (I forget it in the briefing, Sorry) please add it to the drafts.
=> "84116 Grunwiesel"
The Name under the Logo ("Lukas Wendorf") looks like a little to big/wide on the right side, please let it start and end on the exact same width that the Logo is.
The "Background" of the Flyer with the integrated Business Card can't be complete blue, there will be some Text added in the future, it's a information Flyer with some facts about my work and so on, so there must be some space for these texts. The Businesscard "in" the Flyer must the same Card as the normal Business card, except the round corners.
The Dimensions from all the stuff is like the given Dimensions from the attached Information-PDF's?
OK, the price is guaranteed! I would upgrade this project, the Problem is I must pay with coinrelay, and in Germany you send via echeck the money from your regular bank account to coinrelay. But this way need very very long here on zentrofix.example (I don't know why), i paid this project on the 16. feb, today (25. fe) the project started, ~7 workdays for clearing the echeck. So, when I now pay the Guaranteed-Upgrade the project-option will confirmed when the project ends ...
The Logo itself comes from my first project here on zentrofix.example, and there was the price guaranteed, too.
#22 - Can you please add on the backside the url's like on #7 ?
@quembrastudio
#18 - Businesscard: The footer (colored fields) maybe a little bit to strong/high, can you test it with 2-3px less?
#18 - Letterheadpaper: Need the footer (colored fields) here! Looks without ... nacked. ;)
#18 - Please add the "Back of the business card"-things what you can read in the briefing.
#1 #2 - Eliminated; Better draft available with #4
#11 - Eliminated; I think the logo is better on a "normal" business card style, and maybe thats are other card Dimensions.
#10 #9 - The Black Symbols on the Businesscard is maybe to strong. Can you test it with blue or grey symbols?
#4 - At the moment my favorite, but please the "84116 Grunwiesel" in a new line under the Street (businesscard), thats the correct format in Germany. I'm not so happy with the URL in the blue footerfield, maybe smaller or in a other location, I don't know?! Please put on the letterhead the Facts from the footer into the header (right under the Logo), maybe in a small/tiny clear Fonttype. The Flyerbusinesscard don't have the color fields on the bottom?
@torven
#8 - Front looks nice, but the Logo on the backside is not strong/"clear" enough I think.
#7 #5 - Eliminated; Not my Style, Sorry.
#6 - Eliminated; The footer (blue field) on the Front was to heavy
So, trust me or not.
--- Gerold

```html
<!DOCTYPE html>
<html lang="de">
<head>
<meta charset="utf-8">
<title>Lukas Wendorf – Briefpapier</title>
<link rel="stylesheet" href="https://fonts.googleapis.com/css2?family=Open+Sans:wght@400;600;700&display=swap">
<style>
  :root {
    --stage: #ececea;
    --paper: #ffffff;
    --brand-blue: #1f6fc1;
    --brand-blue-dark: #164f8c;
    --brand-grey: #4a4f57;
    --text-small: #6b7079;
    --mark-faint: #e9ecf1;
    --rule: #d7dbe1;
  }
  * { margin: 0; padding: 0; box-sizing: border-box; }
  html, body {
    width: 1200px; height: 638px; overflow: hidden;
    background: var(--stage);
    font-family: "Open Sans", Arial, sans-serif;
  }
  .canvas { position: relative; width: 1200px; height: 638px; }

  .sheet {
    position: absolute; top: 55px;
    width: 370px; height: 528px;
    background: var(--paper);
    overflow: hidden;
    box-shadow: 0 2px 8px rgba(0,0,0,.18);
  }
  .sheet--plain   { left: 30px; }
  .sheet--centred { left: 415px; }
  .sheet--details { left: 800px; }

  .brand {
    position: absolute; top: 22px;
    display: flex; align-items: center; gap: 6px;
    color: var(--brand-blue); font-weight: 700; font-size: 13px; letter-spacing: .2px;
  }
  .brand__square { width: 11px; height: 11px; background: var(--brand-blue); }
  .sheet--plain .brand, .sheet--details .brand { left: 16px; }
  .sheet--centred .brand { left: 50%; transform: translateX(-50%); }

  .header-rule {
    position: absolute; left: 16px; right: 16px; top: 48px;
    height: 1px; background: var(--brand-blue);
  }
  .sheet--plain .header-rule { background: var(--rule); }
  .sheet--details .header-rule { display: none; }

  .sender {
    position: absolute; right: 16px; top: 14px;
    text-align: right; font-size: 5px; line-height: 7.6px; color: var(--text-small);
  }
  .sender strong { color: var(--brand-grey); font-weight: 700; }

  .watermark {
    position: absolute; color: var(--mark-faint);
    font-weight: 700; white-space: nowrap; line-height: 1;
  }
  .sheet--plain .watermark { left: 130px; bottom: 6px; font-size: 46px; }
  .sheet--centred .watermark,
  .sheet--details .watermark { left: 50%; top: 205px; transform: translateX(-50%); font-size: 46px; }

  .footer {
    position: absolute; left: 16px; right: 16px; bottom: 12px;
    font-size: 4.6px; line-height: 7px; color: var(--text-small);
  }
  .footer strong { color: var(--brand-grey); font-weight: 700; }
  .footer a { color: var(--brand-blue); text-decoration: none; font-weight: 600; }
  .sheet--centred .footer, .sheet--details .footer { text-align: center; }

  .footer-band {
    position: absolute; left: 0; right: 0; bottom: 0; height: 4px;
    display: flex;
  }
  .footer-band__main { flex: 1; background: var(--brand-blue); }
  .footer-band__accent { width: 30%; background: var(--brand-blue-dark); }
</style>
</head>
<body>
<main class="canvas">

  <section class="sheet sheet--plain">
    <div class="brand"><span class="brand__square"></span>Lukas Wendorf</div>
    <div class="header-rule"></div>
    <div class="watermark" aria-hidden="true">Lukas Wendorf</div>
    <footer class="footer">
      <p><strong>Lukas Wendorf</strong> | Birkenweg 12 | 84116 Grunwiesel | T +49 871 2040 | F +49 871 2041</p>
      <p>E info@wendorf.example | W <a>www.wendorf.example</a></p>
    </footer>
    <div class="footer-band"><span class="footer-band__main"></span><span class="footer-band__accent"></span></div>
  </section>

  <section class="sheet sheet--centred">
    <div class="brand"><span class="brand__square"></span>Lukas Wendorf</div>
    <div class="header-rule"></div>
    <div class="watermark" aria-hidden="true">Lukas Wendorf</div>
    <footer class="footer">
      <p><strong>Lukas Wendorf</strong> | Birkenweg 12 | 84116 Grunwiesel | T +49 871 2040 | F +49 871 2041</p>
      <p>E info@wendorf.example | W <a>www.wendorf.example</a></p>
    </footer>
    <div class="footer-band"><span class="footer-band__main"></span><span class="footer-band__accent"></span></div>
  </section>

  <section class="sheet sheet--details">
    <div class="brand"><span class="brand__square"></span>Lukas Wendorf</div>
    <address class="sender">
      <strong>Lukas Wendorf</strong><br>
      Birkenweg 12<br>
      84116 Grunwiesel<br>
      T +49 871 2040<br>
      F +49 871 2041<br>
      info@wendorf.example<br>
      <strong>www.wendorf.example</strong>
    </address>
    <div class="watermark" aria-hidden="true">Lukas Wendorf</div>
    <footer class="footer">
      <p><strong>Lukas Wendorf</strong> | Birkenweg 12 | 84116 Grunwiesel | T +49 871 2040 | F +49 871 2041</p>
      <p>E info@wendorf.example | W <a>www.wendorf.example</a></p>
    </footer>
    <div class="footer-band"><span class="footer-band__main"></span><span class="footer-band__accent"></span></div>
  </section>

</main>
</body>
</html>
```